Property Finance Company - Orin Ventures Limited

Background: Orin Ventures Group Limited is a private property finance company. Orin Ventures Group has capital to directly fund first mortgage, mezzanine and preferred equity financing. We also acquire performing, sub-performing and distressed debt.

Orin Ventures' management philosophy emphasises expertise, innovation, wisdom, honesty and competitiveness. Orin Ventures are not finance brokers - we provide debt funding to the commercial property and residential development sectors. Our process is built from experience and cumutavely Orin Ventures' Directors have in excess of 60 years wisdom.

The aim of the website will be to increase brand awareness, provide clients with comfort around our level of skill and background on who we are, generate more sales, and provide examples of projects that we have funded.

The website is a new product launch, and we need to use our Orin Ventures logo that has just been designed. We like a dark background, and either black/silver/grey/ jade green, or black/gold/jade green colours.

Our unique advantages are that we have fast turnaround times, we can solve clients funding problems and we know what we are doing. Our target audience will be viewing the website on both desktop and mobile devices.

We would like to have the following pages:

Home
About
Team
Services
Project Experience
Contact

Competitors Website: http://www.tarvelo.com/

We would also like to have the option of video footage in our website, as you can see in our competitors website.

Overall we want a really slick, elegant but modern website that is better than www.tarvelo.com

Target Market(s)

Finance borrowers, property developers, accountants, lawyers, businesspeople, high net worth people

Industry/Entity Type

Finance

Requirements
Must have
• Please see project description
Nice to have
Should not have

```html
<!DOCTYPE html>
<html lang="en">
<head>
<meta charset="utf-8">
<title>Orin Ventures Limited — Our Story</title>
<link href="https://fonts.googleapis.com/css2?family=Poppins:wght@400;500;600;700&family=Open+Sans:wght@400;600;700&display=swap" rel="stylesheet">
<style>
:root{
  --gold:#f2b522;
  --gold-soft:#f6c545;
  --green:#2fb84e;
  --green-light:#7ad94a;
  --ink:#1c1c1c;
  --text:#555;
  --muted:#9a9a9a;
  --line:#e3e3e3;
  --paper:#ffffff;
  --grey-bg:#f0f0f0;
  --footer:#151515;
}
*{box-sizing:border-box;margin:0;padding:0}
html,body{width:1200px;height:4580px;overflow:hidden}
body{font-family:"Open Sans",Arial,sans-serif;color:var(--text);background:var(--paper);position:relative}
h1,h2,h3,h4,.display{font-family:"Poppins",Arial,sans-serif;color:var(--ink)}
section,header,footer{position:absolute;left:0;width:1200px}
.photo{position:absolute}
.section-title{text-align:center;font-size:34px;font-weight:600}
.section-lead{width:640px;margin:14px auto 0;text-align:center;font-size:14px;line-height:22px;color:var(--muted)}

/* hero */
.hero{top:0;height:755px;background:linear-gradient(180deg,#4a4036 0%,#2f2a25 60%,#1d1b19 100%);overflow:hidden}
.hero .photo{inset:0;background:radial-gradient(ellipse at 30% 30%,#6d5e4d 0%,transparent 55%),radial-gradient(ellipse at 80% 40%,#5a4f44 0%,transparent 50%);opacity:.9}
.hero .shade{position:absolute;inset:0;background:rgba(15,15,15,.35)}
.menu{position:absolute;right:40px;top:22px;width:26px}
.menu span{display:block;height:3px;background:#fff;margin-bottom:5px}
.brand{position:absolute;left:0;width:1200px;top:240px;text-align:center}
.brand .mark{width:46px;height:46px;border-radius:50%;border:2px solid #fff;margin:0 auto 12px}
.brand .name{font-family:"Poppins",sans-serif;font-size:20px;font-weight:600;color:#fff;letter-spacing:2px}
.hero h1{position:absolute;top:375px;width:1200px;text-align:center;color:#fff;font-size:74px;font-weight:700}
.hero .tag{position:absolute;top:470px;width:1200px;text-align:center;color:var(--gold);font-size:15px}
.play{position:absolute;left:567px;top:515px;width:66px;height:66px;border-radius:50%;background:#222}

/* what we do */
.what{top:755px;height:445px}
.what .section-title{margin-top:60px}
.services{position:absolute;top:200px;left:190px;width:820px;display:flex;justify-content:space-between}
.service{width:240px;text-align:center}
.service svg{display:block;margin:0 auto 10px}
.service h3{font-size:17px;font-weight:500;line-height:22px}
.service p{font-size:12px;line-height:18px;color:var(--muted);margin-top:8px}

/* knowledge */
.knowledge{top:1200px;height:630px;background:var(--grey-bg);overflow:hidden}
.knowledge .photo.office{right:0;top:0;width:1200px;height:630px;background:linear-gradient(90deg,#eee 0%,#e6e6e6 45%,#d6d6d6 100%);opacity:.7}
.quote{position:absolute;left:110px;top:205px;width:360px}
.quote h2{font-size:22px;font-weight:500;line-height:30px}
.quote .by{font-size:12px;font-weight:700;color:var(--ink);margin-top:6px;letter-spacing:.5px}
.quote p{font-size:13px;line-height:20px;color:var(--muted);margin-top:24px}
.knowledge .photo.woman{left:470px;top:370px;width:210px;height:260px;background:linear-gradient(180deg,#d9d4cf,#b8b0a8)}
.pie{position:absolute;left:635px;top:30px}

/* how it works */
.how{top:1830px;height:480px}
.how .section-title{margin-top:45px}
.timeline{position:absolute;top:165px;left:110px;width:980px;height:60px}
.timeline .rail{position:absolute;left:0;right:0;top:42px;height:2px;background:var(--line)}
.timeline .done{position:absolute;left:0;width:120px;top:41px;height:4px;background:var(--green)}
.step{position:absolute;width:220px;text-align:center;top:0;margin-left:-110px}
.step b{display:block;font-family:"Poppins",sans-serif;font-size:14px;font-weight:600;color:var(--green)}
.step span{display:block;font-size:11px;color:var(--muted);margin-top:2px}
.dot{position:absolute;top:35px;left:110px;margin-left:-8px;width:16px;height:16px;border-radius:50%;background:var(--green)}
.solution{position:absolute;left:110px;top:290px;width:620px}
.solution h3{font-size:14px;font-weight:600;text-transform:uppercase}
.solution p{font-size:12.5px;line-height:20px;color:var(--muted);margin-top:12px}
.checklist{position:absolute;left:790px;top:285px;list-style:none}
.checklist li{font-size:12.5px;line-height:26px;color:var(--muted);padding-left:18px;position:relative}
.checklist li::before{content:"";position:absolute;left:0;top:10px;width:7px;height:7px;border-radius:50%;background:var(--gold)}

/* team */
.team{top:2310px;height:565px}
.team .section-title{margin-top:20px}
.member{position:absolute;top:185px;width:250px}
.member .photo{position:relative;height:280px;background:linear-gradient(180deg,#f4f4f4,#e2e2e2)}
.member .photo.light::after{content:"";position:absolute;left:50px;right:50px;bottom:0;height:190px;background:linear-gradient(180deg,#8a7d72,#3d3a3a);border-radius:90px 90px 0 0}
.member.featured .photo{background:var(--gold)}
.member.featured .photo .hover{position:absolute;left:20px;bottom:30px;color:#fff;font-size:12px;line-height:18px}
.member h4{font-size:15px;font-weight:500;margin-top:14px}
.member p{font-size:11px;color:var(--muted)}

/* call band */
.call{top:2875px;height:450px;background:linear-gradient(180deg,#4cd64a 0%,#2fc27a 45%,#c8f0c9 80%,#ffffff 100%)}
.call .phone{position:absolute;top:75px;width:1200px;text-align:center;color:#fff;font-size:42px;font-weight:600;letter-spacing:2px}
.call .call-tag{position:absolute;top:138px;width:1200px;text-align:center;color:#fff;font-size:13px;font-weight:600;letter-spacing:.5px}
.call h2{position:absolute;top:270px;width:1200px;text-align:center;color:#fff;font-size:34px;font-weight:600}
.call .section-lead{position:absolute;top:320px;left:280px;color:#f2fff2;margin:0}

/* projects */
.projects{top:3320px;height:255px;display:flex}
.projects .photo{position:relative;flex:1;height:255px}
.proj-a{background:linear-gradient(180deg,#6f8fb5 0%,#a8413a 60%,#5b5b5b 100%)}
.proj-b{background:linear-gradient(180deg,#8aa7c8 0%,#b5462f 50%,#7a3a2a 100%)}
.proj-c{background:linear-gradient(180deg,#7fa6cf 0%,#9b8a78 55%,#3d3d3f 100%)}

/* testimonials */
.voices{top:3575px;height:500px;overflow:hidden}
.voices .section-title{margin-top:70px}
.bubble{position:absolute;top:210px;left:260px;width:680px;height:190px;background:#fff;border-radius:6px;box-shadow:0 6px 24px rgba(0,0,0,.1);padding:28px 40px}
.bubble p{font-size:12.5px;line-height:20px;color:var(--muted);text-align:center}
.author{position:absolute;left:40px;bottom:24px;display:flex;align-items:center}
.author i{width:36px;height:36px;border-radius:50%;background:#c6bdb4;margin-right:10px}
.author b{display:block;font-size:11px;color:var(--ink)}
.author span{display:block;font-size:10px;color:var(--muted)}
.dots{position:absolute;top:435px;width:1200px;display:flex;justify-content:center;gap:6px}
.dots i{width:8px;height:8px;border-radius:50%;background:#ddd}
.dots i.on{background:var(--gold)}
.ring{position:absolute;border:2px solid #f1f1f1;border-radius:50%}

/* footer */
.site-footer{top:4075px;height:505px;background:var(--footer);color:#8c8c8c}
.follow{position:absolute;top:30px;width:1200px;text-align:center;color:#fff;font-size:12px;font-weight:600}
.socials{position:absolute;top:60px;width:1200px;display:flex;justify-content:center;gap:14px}
.socials i{width:32px;height:32px;border-radius:50%;border:1px solid #555}
.cols{position:absolute;top:215px;left:110px;width:980px;display:flex;justify-content:space-between}
.col{width:210px}
.col h4{color:#fff;font-size:12px;font-weight:600;letter-spacing:1px}
.col h4::after{content:"";display:block;width:24px;height:2px;background:var(--gold);margin-top:8px}
.col p,.col li{font-size:11px;line-height:19px;margin-top:12px;list-style:none}
.col li{margin-top:4px}
.col .field{height:26px;border:1px solid #444;margin-top:12px}
.copyright{position:absolute;bottom:0;width:1200px;height:50px;line-height:50px;border-top:1px solid #2a2a2a;text-align:center;font-size:11px}
</style>
</head>
<body>

<header class="hero">
  <div class="photo" role="img" aria-label="Team of professionals meeting around a table in a bright office"></div>
  <div class="shade"></div>
  <div class="menu"><span></span><span></span><span></span></div>
  <div class="brand"><div class="mark"></div><div class="name">ORIN VENTURES</div></div>
  <h1>Our Story</h1>
  <div class="tag">scales of 60 years wisdom</div>
  <div class="play"><svg width="66" height="66" viewBox="0 0 66 66"><path d="M28 23 L44 33 L28 43 Z" fill="#fff"/></svg></div>
</header>

<section class="what">
  <h2 class="section-title">What We Do?</h2>
  <p class="section-lead">We fund first mortgage, mezzanine and preferred equity for property projects, and we move quickly so our clients can move forward with confidence.</p>
  <div class="services">
    <div class="service">
      <svg width="30" height="30" viewBox="0 0 30 30"><rect x="4" y="16" width="5" height="10" fill="var(--gold)"/><rect x="12" y="10" width="5" height="16" fill="var(--gold)"/><rect x="20" y="5" width="5" height="21" fill="var(--gold)"/></svg>
      <h3>Debt<br>Funding</h3>
      <p>Direct lending with clear terms and a fast, reliable turnaround.</p>
    </div>
    <div class="service">
      <svg width="30" height="30" viewBox="0 0 30 30"><rect x="7" y="4" width="16" height="22" fill="var(--gold)"/><rect x="10" y="8" width="3" height="3" fill="#fff"/><rect x="17" y="8" width="3" height="3" fill="#fff"/><rect x="10" y="14" width="3" height="3" fill="#fff"/><rect x="17" y="14" width="3" height="3" fill="#fff"/></svg>
      <h3>commercial property<br>Funding</h3>
      <p>Capital for offices, retail and industrial assets of every size.</p>
    </div>
    <div class="service">
      <svg width="30" height="30" viewBox="0 0 30 30"><circle cx="15" cy="15" r="11" fill="var(--gold)"/><path d="M4 15 H26 M15 4 V26" stroke="#fff" stroke-width="1.5"/></svg>
      <h3>residential development<br>Funding</h3>
      <p>Support for housing projects from land purchase to completion.</p>
    </div>
  </div>
</section>

<section class="knowledge">
  <div class="photo office" role="img" aria-label="Soft office interior backdrop"></div>
  <div class="quote">
    <h2>AN INVESTMENT IN KNOWLEDGE PAYS THE BEST INTEREST.</h2>
    <div class="by">— HARLAN WHITCOMBE</div>
    <p>Our directors bring decades of lending experience to every deal, so each loan is shaped with care, clear judgement and honest advice from the first call to final settlement.</p>
  </div>
  <div class="photo woman" role="img" aria-label="Businesswoman working at a laptop"></div>
  <svg class="pie" width="570" height="570" viewBox="0 0 570 570">
    <path d="M280 280 L280 10 A270 270 0 0 0 10 280 Z" fill="var(--gold)"/>
    <path d="M290 280 L290 10 A270 270 0 0 1 560 280 Z" fill="#b9a995" role="img" aria-label="Colleagues meeting at a desk"/>
    <path d="M280 290 L10 290 A270 270 0 0 0 280 560 Z" fill="#cfc8c1" role="img" aria-label="Advisor at a bright workspace"/>
    <path d="M290 290 L560 290 A270 270 0 0 1 290 560 Z" fill="var(--gold)"/>
    <circle cx="180" cy="160" r="6" fill="none" stroke="#fff" stroke-width="2"/>
    <text x="180" y="195" fill="#fff" font-family="Open Sans, sans-serif" font-size="13" text-anchor="middle">Orin Expertise in service</text>
    <text x="180" y="213" fill="#fff" font-family="Open Sans, sans-serif" font-size="13" text-anchor="middle">through</text>
    <text x="180" y="231" fill="#fff" font-family="Open Sans, sans-serif" font-size="13" text-anchor="middle">our experience</text>
    <circle cx="395" cy="350" r="6" fill="none" stroke="#fff" stroke-width="2"/>
    <text x="395" y="385" fill="#fff" font-family="Open Sans, sans-serif" font-size="13" text-anchor="middle">Our Team for your</text>
    <text x="395" y="403" fill="#fff" font-family="Open Sans, sans-serif" font-size="13" text-anchor="middle">Development</text>
  </svg>
</section>

<section class="how">
  <h2 class="section-title">How It Works</h2>
  <p class="section-lead">A simple four stage process that takes each project from first conversation to funded, without delay or surprises.</p>
  <div class="timeline">
    <div class="rail"></div><div class="done"></div>
    <div class="step" style="left:110px"><b>PLAN</b><span>Review goals and scope</span></div>
    <div class="step" style="left:360px"><b>ANALYZE</b><span>Assess risk and value</span></div>
    <div class="step" style="left:610px"><b>CREATE</b><span>Structure the facility</span></div>
    <div class="step" style="left:860px"><b>SAVE</b><span>Settle and deliver funds</span></div>
    <div class="dot"></div>
  </div>
  <div class="solution">
    <h3>A better solution for your financial needs</h3>
    <p>We are direct lenders, not brokers. Decisions are made by people who know property and finance, so approvals are quick and terms are clear. We look at the whole picture, including the site, the plan and the people, and we work with borrowers to solve funding problems that others will not take on.</p>
  </div>
  <ul class="checklist">
    <li>Certain Budget</li>
    <li>No Hidden Expenses</li>
    <li>Fast turnaround times</li>
    <li>Clear approval path</li>
    <li>All our business</li>
    <li>Team supported</li>
  </ul>
</section>

<section class="team">
  <h2 class="section-title">Our Team</h2>
  <p class="section-lead">Experienced directors and advisors who bring decades of property lending knowledge to every project.</p>
  <div class="member" style="left:100px">
    <div class="photo light" role="img" aria-label="Portrait of a team member"></div>
    <h4>Marisa Calloway</h4><p>Senior Client Manager</p>
  </div>
  <div class="member featured" style="left:460px">
    <div class="photo" role="img" aria-label="Portrait of a team member"><div class="hover">Read Profile<br>View details</div></div>
    <h4>Elena Varga</h4><p>Investment Director</p>
  </div>
  <div class="member" style="left:815px">
    <div class="photo light" role="img" aria-label="Portrait of a team member"></div>
    <h4>Sabine Foss</h4><p>Senior Credit Analyst</p>
  </div>
</section>

<section class="call">
  <div class="phone display">1800 555 019 42</div>
  <div class="call-tag">CHAT WITH US FOR YOUR BEST SOLUTION IN FINANCE</div>
  <h2>Our Projects</h2>
  <p class="section-lead">A selection of commercial and residential developments we have funded across the region.</p>
</section>

<section class="projects">
  <div class="photo proj-a" role="img" aria-label="Modern commercial building with red facade"></div>
  <div class="photo proj-b" role="img" aria-label="Brick office building under blue sky"></div>
  <div class="photo proj-c" role="img" aria-label="City skyline with tall towers"></div>
</section>

<section class="voices">
  <div class="ring" style="left:120px;top:180px;width:200px;height:200px"></div>
  <div class="ring" style="left:880px;top:240px;width:220px;height:220px"></div>
  <h2 class="section-title">What Customers Are Saying</h2>
  <p class="section-lead">Borrowers, developers and advisors share what it is like to work with our team.</p>
  <div class="bubble">
    <p>Orin Ventures understood our project from day one. Approval came quickly, the terms were clear and the team stayed in touch at every stage. We finished on schedule and would gladly work with them again on our next development.</p>
    <div class="author"><i></i><div><b>Ava M.</b><span>Property Developer</span></div></div>
  </div>
  <div class="dots"><i class="on"></i><i></i><i></i></div>
</section>

<footer class="site-footer">
  <div class="follow">Follow Us</div>
  <div class="socials"><i></i><i></i><i></i><i></i></div>
  <div class="cols">
    <div class="col"><h4>ABOUT US</h4><p>Orin Ventures Group Limited is a private property finance company providing direct debt funding to developers.</p></div>
    <div class="col"><h4>SITEMAP</h4><ul><li>Home</li><li>About</li><li>Services</li><li>Projects</li><li>Contact</li></ul></div>
    <div class="col"><h4>CONTACT INFO</h4><ul><li>14 Harbour Lane, Suite 3</li><li>1800 555 019 42</li><li>hello@orinventures.example</li></ul></div>
    <div class="col"><h4>NEWSLETTER</h4><p>Get updates on new projects and offers.</p><div class="field"></div></div>
  </div>
  <div class="copyright">© 2024 Orin Ventures. All rights reserved.</div>
</footer>

</body>
</html>
```